Graphic Design Layout For Funeral Home App (The Contest is for the homepage of the App Only) Additional pages based off design

The purpose of this app:

For the purposes of this contest, I am looking for the design of the Home page of the App. What will people see when they download the app and see the first page. I describe it in much more detail below but here are the elements of the home page.

1. Picture of the deceased (3 smaller thumbnail photos
2. Date of Birth and date of passing
3. A short statement or statements about the person's life.
4. View the obituary button
5. View the Service Information button
5. Name of the funeral home and contact information, address, email, phone number, chat

The information below will help you to better understand the purpose of the app.

When a family goes into a funeral home to make arrangement for their family member who just passed away. We want an app where we can:
1. Put the decease person’s pictures, Their name, The name of the funeral home, The representative of the funeral home that people can contact, phone number of funeral home, when the funeral service is open and other information in relationship to the funeral, the viewing, contact person for the family etc....

The Layout needs to be powerful but not overwhelming. I am providing some ideas of what the layout should look like but please add your creativeness to the project.

Design of the App

First, when a person receives the link about a deceased person, first comes the focus will be to focus on the decease person who is going to be featured when the link is sent out to family members and extended family and friends.

• So that would be a picture of the decease person
• Date Of birth – Date Of passing
• One statement below that, that describes the person’s life. For example:
He was the best, Husband, Father and Friend.
• Below that it will say View Obituary and Service Information
• Below that will be 3 small thumbnail pictures below the main picture
• Share (Button) (share this link on chirpwave, palbook, worknexus, phone number, contact list, etc…)
• Funeral Home Name with contact phone and email.

This will be the initial focus of the first page. It is primarily focused on the deceased.
Once they click any of the information on the first page then they will see additional options when they go to see the obituary and service information.
They will see:

• RSVP (you will be able to RSVP to let the family know that you are coming). (It will show how
many people have RSVP)
• Send Flowers To The Family (This will allow you to purchase flowers and send them to the
family)
• Sign Registry Book
• Below That it will say Contact Funeral Home

It will have a small picture of the funeral home representative
A small statement from them saying: Thank you for allowing our funeral home to serve you. If you have any questions don’t hesitate to contact us.
The phone number and email address.
• Below that would be a Online Chat button where they can chat with the funeral home
representative.

When you click on the View Service Information

It will take you to the next page where you will have the obituary: You will initial only see a couple of sentences but you can expand it to see more.

Below the obituary
Family Tribute
Below the obituary will be a picture of each family member that has been submitted and statements that they have made concerning the deceased.
Next to the family members name and picture there is a send condolences link.
A person can click on that and send condolences to the person they are familiar with. There will be an option to send condolences to the entire family or just an individual family member.

Friends & Community Tribute
These will be comments that are made by friends and associates in the community. (they can upload their picture or have a silhouette of a picture
People will be able to make comments and people can go in and like the comments and make piggy back comments on the comments that were made.

```html
<!DOCTYPE html>
<html lang="en">
<head>
<meta charset="utf-8">
<title>Memorial App — Home</title>
<link rel="stylesheet" href="https://fonts.googleapis.com/css2?family=Roboto:wght@300;400;500;700&display=swap">
<style>
:root{
  --canvas:#ffffff;
  --teal:#1a9e8f;
  --violet:#5b2fd6;
  --violet-2:#7a45f0;
  --light-bg:#ffffff;
  --light-ink:#2b2b2b;
  --light-muted:#7a7a7a;
  --dark-bg:#232323;
  --dark-ink:#f1f1f1;
  --dark-muted:#bdbdbd;
  --icon:#5a5a5a;
}
*{margin:0;padding:0;box-sizing:border-box}
html,body{width:1200px;height:2512px;overflow:hidden;background:var(--canvas);font-family:"Roboto",sans-serif}
.stage{position:relative;width:1200px;height:2512px}
.screen{position:absolute;top:433px;width:520px;height:1645px;overflow:hidden;
  --bg:var(--light-bg);--ink:var(--light-ink);--muted:var(--light-muted);--ic:var(--icon);
  background:var(--bg);box-shadow:0 6px 24px rgba(0,0,0,.12)}
.screen--light{left:60px}
.screen--dark{left:620px;--bg:var(--dark-bg);--ink:var(--dark-ink);--muted:var(--dark-muted);--ic:#d0d0d0}
.hero{position:absolute;left:0;top:0;width:520px;height:670px;
  background:radial-gradient(ellipse 40% 34% at 50% 36%,#8a8a8a 0%,#5c5c5c 55%,transparent 100%),
             linear-gradient(180deg,#3a3a3a 0%,#2c2c2c 45%,#4a4a4a 78%,var(--bg) 100%)}
.menu{position:absolute;left:32px;top:63px}
.more{position:absolute;right:26px;top:60px}
.name{position:absolute;left:32px;top:583px;font-size:28px;font-weight:700;color:var(--ink);letter-spacing:.3px}
.meta{position:absolute;left:32px;font-size:21px;font-weight:300;color:var(--muted)}
.thumbs{position:absolute;left:32px;top:678px;display:flex;gap:6px}
.thumb{height:113px;background:linear-gradient(160deg,#2e2e2e,#7b7b7b 55%,#3a3a3a)}
.thumb--wide{width:220px}.thumb--sq{width:113px}
.thumb--pale{background:linear-gradient(180deg,#bdbdbd,#e2e2e2 60%,#cfcfcf)}
.label{position:absolute;left:32px;font-size:21px;font-weight:300;color:var(--teal)}
.event{position:absolute;left:32px;display:flex;gap:18px;align-items:flex-start}
.event svg{margin-top:6px;flex:none}
.event-date{font-size:27px;color:var(--ink);line-height:1.1}
.event-place{font-size:20px;font-weight:300;color:var(--muted)}
.about{position:absolute;left:32px;top:1066px;width:460px;font-size:21px;font-weight:300;line-height:33px;color:var(--muted)}
.tabs{position:absolute;left:32px;top:1226px;width:456px;display:flex;justify-content:space-between;font-size:21px;color:var(--ink)}
.tab--active{color:var(--teal);position:relative}
.tab--active::after{content:"";position:absolute;left:28px;right:28px;top:28px;height:3px;background:var(--teal)}
.home-title{position:absolute;left:33px;top:1302px;font-size:27px;color:var(--ink)}
.contact{position:absolute;left:33px;display:flex;gap:16px;font-size:21px;font-weight:300;color:var(--muted);line-height:28px}
.contact svg{margin-top:5px;flex:none}
.chat{position:absolute;left:32px;top:1507px;width:189px;height:39px;border-radius:20px;
  background:linear-gradient(90deg,var(--violet),var(--violet-2));color:#fff;font-size:20px;
  display:flex;align-items:center;justify-content:center;gap:10px}
</style>
</head>
<body>
<div class="stage">
  <!-- light theme -->
  <section class="screen screen--light">
    <div class="hero" role="img" aria-label="Black and white portrait of the deceased"></div>
    <svg class="menu" width="30" height="22" viewBox="0 0 30 22"><g stroke="#fff" stroke-width="2.5"><line x1="0" y1="2" x2="30" y2="2"/><line x1="0" y1="11" x2="20" y2="11"/><line x1="0" y1="20" x2="30" y2="20"/></g></svg>
    <svg class="more" width="8" height="30" viewBox="0 0 8 30"><g fill="#fff"><circle cx="4" cy="4" r="3"/><circle cx="4" cy="15" r="3"/><circle cx="4" cy="26" r="3"/></g></svg>
    <h1 class="name">MAREN T. HOLLOWAY</h1>
    <p class="meta" style="top:618px">Ashford Falls, VT 05999</p>
    <p class="meta" style="top:645px">1958 - 2019</p>
    <div class="thumbs">
      <div class="thumb thumb--wide" role="img" aria-label="Photo of the deceased"></div>
      <div class="thumb thumb--sq thumb--pale" role="img" aria-label="Photo of the deceased"></div>
      <div class="thumb thumb--sq" role="img" aria-label="Photo of the deceased"></div>
    </div>
    <p class="label" style="top:811px">Born on</p>
    <div class="event" style="top:846px">
      <svg width="22" height="32" viewBox="0 0 22 32"><g fill="var(--ic)"><circle cx="11" cy="7" r="6"/><path d="M11 14 C4 14 2 20 3 24 L8 22 L11 30 L14 22 L19 24 C20 20 18 14 11 14Z"/></g></svg>
      <div><p class="event-date">May 18, 1958</p><p class="event-place">Ashford Falls, VT, US</p></div>
    </div>
    <p class="label" style="top:921px">Past on</p>
    <div class="event" style="top:957px">
      <svg width="22" height="28" viewBox="0 0 22 28"><g fill="var(--ic)"><rect x="6" y="10" width="10" height="18" rx="2"/><path d="M11 0 C15 4 15 7 11 8 C7 7 7 4 11 0Z"/></g></svg>
      <div><p class="event-date">Apr 06, 2019</p><p class="event-place">Cedarport, WA, US</p></div>
    </div>
    <p class="label" style="top:1036px">About her</p>
    <p class="about">Lorem ipsum dolor sit amet, consectetur adipiscing elit, sed do eiusmod tempor incididunt ut labore et dolore magna aliqua.</p>
    <nav class="tabs"><span class="tab tab--active">ADDRESS</span><span class="tab">OBITUARY</span><span class="tab">SERVICE</span></nav>
    <h2 class="home-title">Funeral Home</h2>
    <div class="contact" style="top:1345px"><svg width="22" height="22" viewBox="0 0 24 24"><path fill="var(--ic)" d="M6.6 10.8a15 15 0 006.6 6.6l2.2-2.2c.3-.3.7-.4 1-.2 1.1.4 2.3.6 3.6.6.6 0 1 .4 1 1V20c0 .6-.4 1-1 1C10.6 21 3 13.4 3 4c0-.6.4-1 1-1h3.5c.6 0 1 .4 1 1 0 1.3.2 2.5.6 3.6.1.3 0 .7-.2 1z"/></svg><span>555-014-2291</span></div>
    <div class="contact" style="top:1385px"><svg width="22" height="18" viewBox="0 0 22 18"><rect x="1" y="1" width="20" height="16" rx="1.5" fill="none" stroke="var(--ic)" stroke-width="2"/><path d="M1 2 L11 10 L21 2" fill="none" stroke="var(--ic)" stroke-width="2"/></svg><span>hello@restfulpines.com</span></div>
    <div class="contact" style="top:1422px"><svg width="22" height="22" viewBox="0 0 24 24"><path fill="var(--ic)" d="M12 2a7 7 0 00-7 7c0 5 7 13 7 13s7-8 7-13a7 7 0 00-7-7zm0 9.5A2.5 2.5 0 1112 6.5a2.5 2.5 0 010 5z"/></svg><span>1120 Willow Bend Road<br>Cedarport, WA 98000, US</span></div>
    <div class="chat"><svg width="22" height="20" viewBox="0 0 24 22"><path fill="#fff" d="M0 9 L24 0 L18 22 L11 14 L18 5 L8 12Z"/></svg>CHAT NOW</div>
  </section>

  <!-- dark theme -->
  <section class="screen screen--dark">
    <div class="hero" role="img" aria-label="Black and white portrait of the deceased"></div>
    <svg class="menu" width="30" height="22" viewBox="0 0 30 22"><g stroke="#fff" stroke-width="2.5"><line x1="0" y1="2" x2="30" y2="2"/><line x1="0" y1="11" x2="20" y2="11"/><line x1="0" y1="20" x2="30" y2="20"/></g></svg>
    <svg class="more" width="8" height="30" viewBox="0 0 8 30"><g fill="#fff"><circle cx="4" cy="4" r="3"/><circle cx="4" cy="15" r="3"/><circle cx="4" cy="26" r="3"/></g></svg>
    <h1 class="name">MAREN T. HOLLOWAY</h1>
    <p class="meta" style="top:618px">Ashford Falls, VT 05999</p>
    <p class="meta" style="top:645px">1958 - 2019</p>
    <div class="thumbs">
      <div class="thumb thumb--wide" role="img" aria-label="Photo of the deceased"></div>
      <div class="thumb thumb--sq thumb--pale" role="img" aria-label="Photo of the deceased"></div>
      <div class="thumb thumb--sq" role="img" aria-label="Photo of the deceased"></div>
    </div>
    <p class="label" style="top:811px">Born on</p>
    <div class="event" style="top:846px">
      <svg width="22" height="32" viewBox="0 0 22 32"><g fill="var(--ic)"><circle cx="11" cy="7" r="6"/><path d="M11 14 C4 14 2 20 3 24 L8 22 L11 30 L14 22 L19 24 C20 20 18 14 11 14Z"/></g></svg>
      <div><p class="event-date">May 18, 1958</p><p class="event-place">Ashford Falls, VT, US</p></div>
    </div>
    <p class="label" style="top:921px">Past on</p>
    <div class="event" style="top:957px">
      <svg width="22" height="28" viewBox="0 0 22 28"><g fill="var(--ic)"><rect x="6" y="10" width="10" height="18" rx="2"/><path d="M11 0 C15 4 15 7 11 8 C7 7 7 4 11 0Z"/></g></svg>
      <div><p class="event-date">Apr 06, 2019</p><p class="event-place">Cedarport, WA, US</p></div>
    </div>
    <p class="label" style="top:1036px">About her</p>
    <p class="about">Lorem ipsum dolor sit amet, consectetur adipiscing elit, sed do eiusmod tempor incididunt ut labore et dolore magna aliqua.</p>
    <nav class="tabs"><span class="tab tab--active">ADDRESS</span><span class="tab">OBITUARY</span><span class="tab">SERVICE</span></nav>
    <h2 class="home-title">Funeral Home</h2>
    <div class="contact" style="top:1345px"><svg width="22" height="22" viewBox="0 0 24 24"><path fill="var(--ic)" d="M6.6 10.8a15 15 0 006.6 6.6l2.2-2.2c.3-.3.7-.4 1-.2 1.1.4 2.3.6 3.6.6.6 0 1 .4 1 1V20c0 .6-.4 1-1 1C10.6 21 3 13.4 3 4c0-.6.4-1 1-1h3.5c.6 0 1 .4 1 1 0 1.3.2 2.5.6 3.6.1.3 0 .7-.2 1z"/></svg><span>555-014-2291</span></div>
    <div class="contact" style="top:1385px"><svg width="22" height="18" viewBox="0 0 22 18"><rect x="1" y="1" width="20" height="16" rx="1.5" fill="none" stroke="var(--ic)" stroke-width="2"/><path d="M1 2 L11 10 L21 2" fill="none" stroke="var(--ic)" stroke-width="2"/></svg><span>hello@restfulpines.com</span></div>
    <div class="contact" style="top:1422px"><svg width="22" height="22" viewBox="0 0 24 24"><path fill="var(--ic)" d="M12 2a7 7 0 00-7 7c0 5 7 13 7 13s7-8 7-13a7 7 0 00-7-7zm0 9.5A2.5 2.5 0 1112 6.5a2.5 2.5 0 010 5z"/></svg><span>1120 Willow Bend Road<br>Cedarport, WA 98000, US</span></div>
    <div class="chat"><svg width="22" height="20" viewBox="0 0 24 22"><path fill="#fff" d="M0 9 L24 0 L18 22 L11 14 L18 5 L8 12Z"/></svg>CHAT NOW</div>
  </section>
</div>
</body>
</html>
```